Funky Retro Membership Brochure

We require an A5 (A4 folded) brochure design that outlines the membership options for FernLoop. FernLoop promotes local businesses via social media and presence on the FernLoop website (www.fernloop-example.com.au) as well as providing networking facilities for the local business to meet and collaborate with each other.

Attached are the various Fernloop logos together with the colour style guide. Please ignore the fonts; just note the colours.

We would like the brochure to have a retro style look. Very funky but professional.

The first page of the brochure is the title page. Logo with the following tagline "Linking and Lifting Local Trade across Sydney's Inner West". Additional Text, "2020 Membership". Please also include"#fernloop" on the title page. This hashtag should be in a retro font on an angle.

The second page refers to what we do. Three section headings and text as follows but will require designers to provide appropriate graphics, for example the FernLoop website inside a computer screen etc.:

FERNLOOP WEBSITE
fernloop-example.com.au is the online, digital showcase of our members and their business. Each member has a dedicated webpage to promote their business. Your member page provides all you contact details, links and social media channels, reviews, logos and more.

GUMNOOK
GumNook is where FernLoop members get together. It’s a business community unlike any other. No selling. No Pressure. And it won’t break the bank. We aim to stop the isolation many business owners feel and encourage genuine connections, where referrals happen naturally.

SOCIAL MEDIA
FernLoop uses social media channels to actively promote the FernLoop community and its members. Not only do we promote the businesses but also provide free promotions and advertising for local community groups, schools and non-for-profit organisations.

The third page provides details of the membership levels and annual fees. The information on the membership categories can be found at https://www.fernloop-example.com.au/membership-levels/ All the information contained on the page should be contained on page three of the brochure.

The final, back page, will contain all of the contact details for FernLoop (also found on the www.fernloop-example.com.au)

Target Market(s)

Local community businesses

Industry/Entity Type

Digital Marketing

Font styles to use
Other font styles liked:
• Retro

Requirements
Must have
• Retro feel - refer to project description
Nice to have
• Refer to project description
Should not have
• Not applicable

```html
<!DOCTYPE html>
<html lang="en">
<head>
<meta charset="utf-8">
<title>FernLoop – Contact</title>
<link rel="stylesheet" href="https://fonts.googleapis.com/css2?family=Anton&family=Poppins:wght@300;400;800&display=swap">
<style>
  :root {
    --cream: #ecdcb8;
    --blue: #5f93b5;
    --blue-stripe: #527f9f;
    --shadow-dark: #1f3a36;
    --shadow-mid: #3c5e5a;
  }
  * { margin: 0; padding: 0; box-sizing: border-box; }
  html, body {
    width: 853px;
    height: 1200px;
    overflow: hidden;
    background: var(--cream);
  }
  .back-page {
    position: relative;
    width: 853px;
    height: 1200px;
    background: var(--cream);
    font-family: "Poppins", sans-serif;
    color: var(--cream);
  }
  .panel {
    position: absolute;
    left: 32px;
    top: 22px;
    width: 790px;
    height: 1132px;
    background-color: var(--blue);
    background-image: repeating-linear-gradient(
      135deg,
      var(--blue) 0px,
      var(--blue) 36px,
      var(--blue-stripe) 36px,
      var(--blue-stripe) 48px
    );
    overflow: hidden;
  }
  .hashtag {
    position: absolute;
    left: 178px;
    top: 325px;
    font-family: "Anton", sans-serif;
    font-size: 104px;
    line-height: 1;
    letter-spacing: 1px;
    color: var(--cream);
    transform: rotate(-11deg);
    transform-origin: left center;
    text-shadow:
      2px 2px 0 var(--shadow-mid),
      4px 4px 0 var(--shadow-mid),
      6px 6px 0 var(--shadow-dark);
  }
  .brand {
    position: absolute;
    left: 73px;
    top: 650px;
    display: flex;
    align-items: center;
    gap: 22px;
  }
  .brand-mark {
    width: 108px;
    height: 108px;
    border-radius: 50%;
    border: 9px solid var(--cream);
  }
  .brand-name {
    font-family: "Poppins", sans-serif;
    font-weight: 400;
    font-size: 48px;
    letter-spacing: 1px;
    color: var(--cream);
  }
  .contact-heading {
    position: absolute;
    left: 80px;
    top: 774px;
    font-weight: 800;
    font-size: 44px;
    line-height: 1.1;
    letter-spacing: 0.5px;
  }
  .contact-list {
    position: absolute;
    left: 74px;
    top: 845px;
    list-style: none;
  }
  .contact-item {
    display: flex;
    align-items: center;
    height: 40px;
    margin-bottom: 29px;
    font-weight: 300;
    font-size: 25px;
    letter-spacing: 0.3px;
  }
  .contact-icon {
    width: 40px;
    height: 40px;
    margin-right: 16px;
    flex: none;
    display: flex;
    align-items: center;
    justify-content: center;
  }
  .contact-icon.at {
    font-size: 36px;
    font-weight: 300;
    line-height: 1;
  }
</style>
</head>
<body>
  <main class="back-page">
    <section class="panel">
      <h1 class="hashtag">#fernloop</h1>

      <div class="brand">
        <span class="brand-mark" aria-hidden="true"></span>
        <span class="brand-name">FERNLOOP</span>
      </div>

      <h2 class="contact-heading">Contact us:</h2>

      <ul class="contact-list">
        <li class="contact-item">
          <span class="contact-icon" aria-hidden="true">
            <svg width="30" height="40" viewBox="0 0 30 40">
              <path d="M10 3 C2 10 2 28 12 36 L18 38" fill="none" stroke="var(--cream)" stroke-width="3.5" stroke-linecap="round"/>
              <rect x="6" y="1" width="6" height="8" rx="2" fill="var(--cream)" transform="rotate(-20 9 5)"/>
              <rect x="14" y="32" width="8" height="6" rx="2" fill="var(--cream)" transform="rotate(20 18 35)"/>
            </svg>
          </span>
          <span class="contact-text">0491 570 006</span>
        </li>
        <li class="contact-item">
          <span class="contact-icon" aria-hidden="true">
            <svg width="36" height="36" viewBox="0 0 36 36">
              <g transform="rotate(-18 18 18)">
                <rect x="3" y="9" width="30" height="19" fill="none" stroke="var(--cream)" stroke-width="1.6"/>
                <path d="M3 9 L18 21 L33 9" fill="none" stroke="var(--cream)" stroke-width="1.6"/>
              </g>
            </svg>
          </span>
          <span class="contact-text">chat@fernloop-example.com.au</span>
        </li>
        <li class="contact-item">
          <span class="contact-icon at" aria-hidden="true">@</span>
          <span class="contact-text">https://www.fernloop-example.com.au/</span>
        </li>
      </ul>
    </section>
  </main>
</body>
</html>
```